Business Card for a mobile physiotherapy company

I need a layout for a business card for a mobile physiotherapy company.
Slogan is "Mobile Physiotherapy - Your Road To Recovery"
Phone number is 867-402-5913
Email VantrePhysio@mailbright.ca (subject to change with website)
Website www.VantrePhysio.ca
My name and credentials: Kent Vantre Kent Vantre, BSc(kin), MPT, CAFCI, IMS
Information maybe included: Direct Billing, Services including Physiotherapy, IMS, acupuncture
Maybe include plain circles
One side with the logo clean and sharp
Other side with details, try not to look too busy, keep everything concise

```html
<!DOCTYPE html>
<html lang="en">
<head>
<meta charset="utf-8">
<title>Vantre Physio – Business Card</title>
<link rel="stylesheet" href="https://fonts.googleapis.com/css2?family=Open+Sans:ital,wght@0,400;0,600;0,700;1,400&family=Cinzel:wght@700&display=swap">
<style>
  :root {
    --backdrop: #3a322d;
    --card: #1b1e22;
    --silver: #d9dadc;
    --text-light: #f1f1f1;
    --brand-blue: #2f5a93;
    --brand-green: #1f6a55;
    --rule: #e6e6e6;
  }
  * { box-sizing: border-box; margin: 0; padding: 0; }
  html, body { width: 1200px; height: 864px; overflow: hidden; }
  body {
    background: var(--backdrop);
    font-family: "Open Sans", Arial, sans-serif;
    display: flex;
    align-items: center;
    justify-content: center;
    gap: 40px;
  }
  .card {
    position: relative;
    width: 540px;
    height: 309px;
    background: var(--card);
    border-radius: 4px;
    box-shadow: 0 10px 24px rgba(0,0,0,0.45);
    overflow: hidden;
  }

  /* Front side */
  .front .social {
    position: absolute; top: 26px; right: 26px;
    display: flex; gap: 6px;
  }
  .front .social span {
    width: 20px; height: 20px; border-radius: 50%;
    background: var(--text-light);
  }
  .front .wordmark {
    position: absolute; top: 86px; left: 0; right: 0;
    display: flex; align-items: center; justify-content: center; gap: 12px;
  }
  .wordmark .mark-square {
    width: 18px; height: 18px; background: currentColor;
  }
  .wordmark .name {
    font-family: "Open Sans", Arial, sans-serif;
    font-weight: 700;
    font-size: 38px;
    letter-spacing: 4px;
    text-transform: uppercase;
  }
  .front .wordmark { color: var(--silver); }
  .front .tagline {
    position: absolute; left: 90px; top: 176px;
    color: var(--text-light);
    font-size: 15px; font-style: italic; line-height: 1.5;
  }
  .front .services { font-style: normal; font-size: 15px; }

  /* Back side */
  .back .identity {
    position: absolute; left: 36px; top: 56px;
    line-height: 1.25;
  }
  .back .person {
    color: var(--brand-blue); font-weight: 700; font-size: 22px;
    text-transform: uppercase;
  }
  .back .credentials { color: var(--brand-blue); font-size: 15px; }
  .back .billing { color: var(--brand-green); font-size: 15px; }
  .back .contact {
    position: absolute; left: 36px; top: 152px;
    list-style: none; color: var(--text-light); font-size: 15px; line-height: 1.5;
  }
  .back .contact li { display: flex; align-items: center; gap: 10px; }
  .back .contact svg { width: 14px; height: 14px; fill: var(--text-light); flex: none; }
  .back .rule {
    position: absolute; left: 36px; right: 36px; top: 222px;
    height: 1px; background: var(--rule);
  }
  .back .website {
    position: absolute; right: 36px; top: 240px;
    color: var(--text-light); font-size: 16px;
  }
  .back .wordmark {
    position: absolute; right: 30px; top: 104px;
    display: flex; align-items: center; gap: 8px;
    color: var(--brand-green);
  }
  .back .wordmark .name { font-size: 26px; letter-spacing: 3px; }
  .back .wordmark .mark-square { width: 14px; height: 14px; }
</style>
</head>
<body>

  <section class="card front" aria-label="Card front">
    <div class="social" aria-label="Social media">
      <span></span><span></span>
    </div>
    <div class="wordmark">
      <span class="mark-square"></span>
      <span class="name">Vantre Physio</span>
    </div>
    <p class="tagline">
      Mobile Physiotherapy - Your Road To Recovery<br>
      <span class="services">Physiotherapy • IMS • Acupuncture</span>
    </p>
  </section>

  <section class="card back" aria-label="Card back">
    <div class="identity">
      <p class="person">Kent Vantre</p>
      <p class="credentials">BSc(kin), MPT, CAFCI, IMS</p>
      <p class="billing">Direct Billing</p>
    </div>
    <ul class="contact">
      <li>
        <svg viewBox="0 0 16 16" aria-hidden="true"><path d="M3.5 1.5l2.5 0 1.2 3-1.6 1.2a8 8 0 0 0 4.7 4.7l1.2-1.6 3 1.2 0 2.5a1.5 1.5 0 0 1-1.5 1.5A12.5 12.5 0 0 1 2 3a1.5 1.5 0 0 1 1.5-1.5z"/></svg>
        867-402-5913
      </li>
      <li>
        <svg viewBox="0 0 16 16" aria-hidden="true"><path d="M1 3h14v10H1z M1.8 3.6L8 8.6l6.2-5" fill="none" stroke="#f1f1f1" stroke-width="1.4"/></svg>
        VantrePhysio@mailbright.ca
      </li>
    </ul>
    <div class="wordmark">
      <span class="mark-square"></span>
      <span class="name">Vantre Physio</span>
    </div>
    <div class="rule"></div>
    <p class="website">www.VantrePhysio.ca</p>
  </section>

</body>
</html>
```